Cyber Security Site Design (Products & Consulting)

I need my website redesigned to be engaging, clean, efficient and modern. My company (when its up and running) is going to be concentrated on two things: a few specific products for cyber security as well as cyber security consulting services. The background I bring to the field is having worked with small companies all the way to the largest government organizations and advising them on their security posture and how to improve it. We need the ability to add products and services easily.

For a sample product, you can use either Heron (http://www.heron-relay.example/) or Vorlant Greystone (https://www.vorlant.example/products/relay-hub-and-layered-access-portal).

It will replace https://talmerocharts.example/

Target Market(s)

Cyber Security professionals in all verticals

Coding

Coded - Design and coding required

Number of Pages Required

4 page

Font styles to use
Sans Serif

Colors
6b449b

Requirements
Must have
• Ability to easily modify
• Have main page
• Have product specific pages
• Have consulting services pages
• Have executive team information
• Clean, modern design
• Usage of the logo and its color scheme
Nice to have
• I like the idea of a left collapsed sidebar (so icons only) that can expand for text.
• I am also open to a very unique landing page, possibly a shape in the middle (hexagons maybe?) with each of the options there.
Should not have
• Nothing that looks like it came out of a hacker movie

```html
<!DOCTYPE html>
<html lang="en">
<head>
<meta charset="utf-8">
<title>Talmero Charts — Cyber Security Products &amp; Consulting</title>
<link rel="stylesheet" href="https://fonts.googleapis.com/css2?family=Open+Sans:wght@300;400;600;700&display=swap">
<style>
:root{
  --purple:#6b449b;
  --purple-dark:#553580;
  --purple-deep:#45296b;
  --ink:#2b2b2b;
  --text:#777;
  --muted:#9a9a9a;
  --line:#e3e3e3;
  --soft:#f4f4f4;
  --white:#fff;
}
*{box-sizing:border-box;margin:0;padding:0}
html,body{width:1200px;height:3696px;overflow:hidden}
body{position:relative;font-family:"Open Sans",Arial,sans-serif;color:var(--text);background:var(--white);font-size:12px;line-height:1.6}
.abs{position:absolute}
p{font-size:11px;line-height:18px;color:var(--text)}

/* header */
.site-header{position:absolute;left:0;top:0;width:1200px;height:94px;background:var(--white)}
.menu-toggle{position:absolute;left:34px;top:40px;width:18px;height:14px}
.menu-toggle span{display:block;height:2px;background:#888;margin-bottom:4px}
.brand{position:absolute;left:160px;top:26px;display:flex;align-items:center;gap:10px}
.brand-mark{width:38px;height:38px;border-radius:50%;background:var(--purple)}
.brand-name{font-size:24px;font-weight:700;color:var(--purple);letter-spacing:1px;line-height:1}
.main-nav{position:absolute;left:734px;top:38px;display:flex;gap:26px;font-size:10px;color:#555;text-transform:uppercase}
.search{position:absolute;left:1018px;top:35px;width:140px;height:24px;border:1px solid var(--line);font-size:10px;color:var(--muted);padding:4px 8px}
.search svg{position:absolute;right:8px;top:6px}

/* hero */
.hero{position:absolute;left:0;top:94px;width:1200px;height:448px;background:linear-gradient(100deg,#4a2b75 0%,#5d3a8c 45%,#6d4aa0 70%,#4d3078 100%)}
.hero-visual{position:absolute;left:560px;top:0;width:640px;height:448px;background:radial-gradient(circle at 55% 48%,rgba(150,170,230,.45) 0%,rgba(110,90,170,.25) 30%,rgba(0,0,0,0) 60%)}
.hero-copy{position:absolute;left:163px;top:100px;width:420px;color:var(--white)}
.hero-kicker{font-size:22px;font-weight:300;line-height:30px}
.hero-title{font-size:25px;font-weight:700;line-height:32px;text-transform:uppercase;margin-bottom:10px}
.hero-copy p{color:#e6dcf2;font-size:11px;line-height:17px;width:410px}
.btn-light{display:inline-block;margin-top:22px;background:var(--white);color:var(--purple);font-size:9px;font-weight:700;text-transform:uppercase;padding:8px 28px}

/* about */
.portrait{position:absolute;left:461px;top:493px;width:276px;height:320px;background:var(--white);padding:10px;box-shadow:0 2px 8px rgba(0,0,0,.12)}
.portrait div{width:100%;height:100%;background:linear-gradient(180deg,#e9e9ea 0%,#d2cfd2 55%,#3c3f4a 100%)}
.section-title{font-size:26px;font-weight:400;color:var(--ink);text-transform:uppercase;letter-spacing:.5px;line-height:1}
.section-title b{font-weight:700}
.section-title .dash{display:inline-block;width:16px;height:3px;background:var(--ink);vertical-align:middle;margin:0 8px 4px 0}
.section-title.center{text-align:center;width:1200px;left:0}
.section-title.center .dash{margin:0 8px 4px}
.about-head{left:163px;top:592px;font-size:24px}
.about-sub{left:163px;top:650px;font-size:13px;font-weight:700;color:var(--ink)}
.about-left{left:163px;top:678px;width:276px}
.about-right{left:761px;top:650px;width:276px}

/* products */
.products{position:absolute;left:0;top:880px;width:1200px;height:488px;background:var(--soft)}
.product-card{position:absolute;top:1000px;width:200px;height:249px;background:var(--white);text-align:center;padding:26px 18px 0;box-shadow:0 1px 4px rgba(0,0,0,.08)}
.product-card .icon{width:50px;height:50px;border-radius:50%;border:1px solid var(--line);margin:0 auto 16px;display:flex;align-items:center;justify-content:center}
.product-card h3{font-size:13px;font-weight:400;color:var(--ink);text-transform:uppercase;line-height:17px;height:40px}
.product-card p{font-size:9px;line-height:13px;margin-top:6px}
.product-card .more{display:inline-block;margin-top:8px;font-size:9px;font-weight:700;color:var(--ink)}
.product-card.active{background:var(--purple)}
.product-card.active .icon{background:var(--white);border-color:var(--white)}
.product-card.active h3,.product-card.active p,.product-card.active .more{color:var(--white)}
.product-card.active .more{border-bottom:1px solid var(--white)}
.dots{position:absolute;display:flex;gap:6px}
.dots i{width:6px;height:6px;border-radius:50%;background:#d4d4d4}
.dots i.on{background:var(--purple)}

/* consulting */
.consult-head{left:163px;top:1428px}
.consult-copy{left:163px;top:1473px;width:420px}
.btn-outline{position:absolute;left:163px;top:1676px;width:170px;height:28px;border:1px solid var(--purple);color:var(--purple);font-size:9px;font-weight:700;text-transform:uppercase;text-align:center;line-height:26px}
.diff-title{left:616px;top:1428px;font-size:15px;color:var(--ink)}
.diff-title:before{content:"";display:inline-block;width:8px;height:2px;background:var(--ink);vertical-align:middle;margin-right:8px}
.accordion{position:absolute;left:616px;top:1464px;width:421px;height:241px;border:1px solid var(--line)}
.acc-row{position:relative;height:30px;line-height:30px;padding-left:8px;font-size:9px;font-weight:700;color:#444;text-transform:uppercase;border-bottom:1px solid var(--line)}
.acc-row .sign{position:absolute;right:10px;top:0;color:var(--purple);font-size:18px;font-weight:400}
.acc-body{height:148px;border-bottom:1px solid var(--line);position:relative}
.acc-body .img{position:absolute;left:5px;top:8px;width:145px;height:134px;background:linear-gradient(160deg,#c9d3e6 0%,#7b8cb0 55%,#3d4560 100%)}
.acc-body p{position:absolute;left:162px;top:8px;width:250px;font-size:9px;line-height:14px}

/* team */
.team{position:absolute;left:0;top:1767px;width:1200px;height:495px;background:var(--purple)}
.team .section-title{color:var(--white)}
.team .section-title .dash{background:var(--white)}
.member{position:absolute;top:1885px;width:200px;height:320px;background:var(--white)}
.member .photo{height:180px;background:linear-gradient(180deg,#eef0f3 0%,#c8ccd4 60%,#6b7283 100%)}
.member h4{font-size:13px;font-weight:400;color:var(--ink);margin:14px 14px 0}
.member .role{font-size:9px;font-weight:700;color:var(--purple);margin:0 14px}
.member p{font-size:9px;line-height:13px;margin:4px 14px 0}
.member .social{display:flex;gap:8px;margin:10px 14px 0}
.member .social i,.follow i{display:block;width:10px;height:10px;background:#bbb}
.v-dots{position:absolute;left:1155px;top:2025px;display:flex;flex-direction:column;gap:10px}
.v-dots i{width:7px;height:7px;border-radius:50%;border:1px solid var(--white)}
.v-dots i.on{background:var(--white)}

/* blog */
.post{position:absolute;top:2390px;width:276px;height:389px;background:var(--white);border:1px solid var(--line)}
.post .img{height:173px;background:linear-gradient(180deg,#3a3a3a 0%,#6e6e6e 50%,#2a2a2a 100%)}
.post .date{position:absolute;left:0;top:0;width:69px;height:49px;background:var(--purple);color:var(--white);padding:4px 8px}
.post .date b{display:block;font-size:18px;line-height:22px}
.post .date span{font-size:9px}
.post .meta{height:27px;background:var(--purple);color:var(--white);font-size:9px;line-height:27px;padding:0 12px;display:flex;justify-content:space-between}
.post h4{font-size:13px;font-weight:700;color:var(--ink);line-height:17px;margin:14px 14px 0}
.post p{font-size:9px;line-height:13px;margin:8px 14px 0}
.post .more{position:absolute;left:14px;top:350px;font-size:9px;font-weight:700;color:var(--ink)}
.btn-load{position:absolute;left:525px;top:2822px;width:150px;height:28px;border:1px solid var(--purple);color:var(--purple);font-size:10px;font-weight:700;text-align:center;line-height:26px}

/* contact */
.contact{position:absolute;left:0;top:2908px;width:1200px;height:406px;background:var(--soft)}
.contact-panel{position:absolute;left:600px;top:0;width:600px;height:406px;background:var(--white);box-shadow:-6px 0 10px rgba(0,0,0,.1)}
.info-label{font-size:11px;font-weight:700;color:var(--purple);text-transform:uppercase}
.info-block{position:absolute;left:163px;width:276px}
.info-block p{font-size:9px;line-height:14px}
.info-block hr{border:0;border-top:1px solid #ddd;margin-top:12px}
.follow{display:flex;gap:14px;margin-top:10px}
.follow i{width:26px;height:26px;background:transparent;border:1px solid #ccc}
.follow i.on{background:var(--purple);border-color:var(--purple)}
.touch-head{left:707px;top:2968px;font-size:22px}
.touch-copy{left:687px;top:3002px;width:300px;font-size:9px;line-height:13px}
.field{position:absolute;height:29px;border:1px solid var(--line);font-size:9px;color:var(--muted);padding:7px 10px 0 24px}
.field svg{position:absolute;left:8px;top:9px}
.btn-submit{position:absolute;left:687px;top:3225px;width:79px;height:30px;background:var(--purple);color:var(--white);font-size:9px;font-weight:700;text-align:center;line-height:30px}

/* footer */
.site-footer{position:absolute;left:0;top:3314px;width:1200px;height:333px;background:var(--purple)}
.footer-brand{position:absolute;left:163px;top:3395px;display:flex;align-items:center;gap:10px}
.footer-brand .brand-mark{background:var(--white)}
.footer-brand .brand-name{color:var(--white)}
.footer-about{left:163px;top:3455px;width:270px}
.footer-about p,.footer-col li,.subscribe p{color:#e2d6f0;font-size:9px;line-height:14px}
.footer-col{position:absolute;top:3373px}
.footer-col h5{font-size:12px;font-weight:700;color:var(--white);text-transform:uppercase;margin-bottom:14px}
.footer-col ul{list-style:none}
.footer-col li{margin-bottom:11px}
.footer-col li.current{text-decoration:underline;color:var(--white)}
.sub-input{position:absolute;left:835px;top:3464px;width:202px;height:30px;border:1px solid #a88dca;color:#e2d6f0;font-size:9px;padding:8px 0 0 26px}
.sub-input svg{position:absolute;left:9px;top:10px}
.btn-send{position:absolute;left:835px;top:3511px;width:65px;height:25px;background:var(--white);color:var(--purple);font-size:9px;font-weight:700;text-align:center;line-height:25px}
.footer-bar{position:absolute;left:0;top:3647px;width:1200px;height:49px;background:var(--purple-deep);color:#d8cbe8;font-size:9px;line-height:49px;padding-left:163px}
</style>
</head>
<body>

<header class="site-header">
  <div class="menu-toggle"><span></span><span></span><span></span></div>
  <div class="brand"><span class="brand-mark"></span><span class="brand-name">TALMERO CHARTS</span></div>
  <nav class="main-nav"><span>Home</span><span>Contact Us</span><span>&#9679; Sign In/Register</span></nav>
  <div class="search">Search
    <svg width="10" height="10" viewBox="0 0 10 10"><circle cx="4" cy="4" r="3" fill="none" stroke="#666" stroke-width="1.3"/><line x1="6.3" y1="6.3" x2="9.3" y2="9.3" stroke="#666" stroke-width="1.3"/></svg>
  </div>
</header>

<section class="hero">
  <div class="hero-visual" role="img" aria-label="Hands holding a tablet with a glowing padlock projected above it"></div>
  <div class="hero-copy">
    <div class="hero-kicker">We Provide</div>
    <h1 class="hero-title">Cyber security as well as<br>consulting services.</h1>
    <p>Talmero Charts, LLC. is a company that takes its roots from the idea of providing appropriate and creative solutions for cyber security operations, development and management. We have a mission first mindset for our clients and their objectives.</p>
    <span class="btn-light">Learn More</span>
  </div>
</section>

<div class="portrait"><div role="img" aria-label="Portrait photo of the company founder"></div></div>

<h2 class="section-title abs about-head"><span class="dash"></span>About <b>Us</b></h2>
<div class="abs about-sub">The professional approach to security</div>
<div class="abs about-left">
  <p>Talmero Charts, LLC. is located in the Elmford | Carran area but are able to work with clients worldwide. Please contact us for any inquiries you may have and we will be glad to assist you in any way possible.</p>
  <p style="margin-top:14px">Duis aute irure dolor in reprehenderit in voluptate velit esse cillum dolore eu fugiat nulla pariatur.</p>
</div>
<div class="abs about-right">
  <p>Sed ut perspiciatis unde omnis iste natus error sit voluptatem accusantium doloremque laudantium, totam rem aperiam, eaque ipsa quae ab illo inventore veritatis et quasi architecto beatae vitae dicta sunt explicabo. Nemo enim ipsam voluptatem quia voluptas sit aspernatur aut.</p>
  <p style="margin-top:14px">Odit aut fugit, sed quia consequuntur magni dolores eos qui ratione voluptatem sequi nesciunt.</p>
</div>

<section class="products"></section>
<h2 class="section-title center abs" style="top:936px"><span class="dash"></span>Products <b>&amp;</b> Services<span class="dash"></span></h2>

<div class="product-card active" style="left:163px">
  <div class="icon"><svg width="22" height="24" viewBox="0 0 22 24"><path d="M11 1 20 4v7c0 6-4 10-9 12C6 21 2 17 2 11V4z" fill="none" stroke="#6b449b" stroke-width="2"/><rect x="8" y="10" width="6" height="6" fill="#6b449b"/></svg></div>
  <h3>Integrated Cyber<br>Defense</h3>
  <p>Excepteur sint occaecat cupidatat non proident, sunt in culpa qui officia deserunt mollit anim id est laborum.</p>
  <span class="more">Read More</span>
</div>
<div class="product-card" style="left:387px">
  <div class="icon"><svg width="22" height="24" viewBox="0 0 22 24"><path d="M11 1 20 4v7c0 6-4 10-9 12C6 21 2 17 2 11V4z" fill="none" stroke="#6b449b" stroke-width="2"/><path d="M7 12l3 3 5-6" fill="none" stroke="#6b449b" stroke-width="2"/></svg></div>
  <h3>Advanced Threat<br>Protection</h3>
  <p>Excepteur sint occaecat cupidatat non proident, sunt in culpa qui officia deserunt mollit anim id est laborum.</p>
  <span class="more">Read More</span>
</div>
<div class="product-card" style="left:611px">
  <div class="icon"><svg width="22" height="22" viewBox="0 0 22 22"><circle cx="11" cy="11" r="9" fill="none" stroke="#6b449b" stroke-width="2"/><rect x="7" y="10" width="8" height="6" fill="#6b449b"/><path d="M8.5 10V8a2.5 2.5 0 0 1 5 0v2" fill="none" stroke="#6b449b" stroke-width="1.6"/></svg></div>
  <h3>Information<br>Protection</h3>
  <p>Excepteur sint occaecat cupidatat non proident, sunt in culpa qui officia deserunt mollit anim id est laborum.</p>
  <span class="more">Read More</span>
</div>
<div class="product-card" style="left:838px">
  <div class="icon"><svg width="24" height="24" viewBox="0 0 24 24"><circle cx="12" cy="12" r="4" fill="#6b449b"/><g stroke="#6b449b" stroke-width="1.6"><line x1="12" y1="2" x2="12" y2="7"/><line x1="12" y1="17" x2="12" y2="22"/><line x1="2" y1="12" x2="7" y2="12"/><line x1="17" y1="12" x2="22" y2="12"/></g><g fill="#6b449b"><circle cx="12" cy="2" r="2"/><circle cx="12" cy="22" r="2"/><circle cx="2" cy="12" r="2"/><circle cx="22" cy="12" r="2"/></g></svg></div>
  <h3>Endpoint<br>Security</h3>
  <p>Excepteur sint occaecat cupidatat non proident, sunt in culpa qui officia deserunt mollit anim id est laborum.</p>
  <span class="more">Read More</span>
</div>
<div class="dots" style="left:582px;top:1305px"><i class="on"></i><i></i><i></i></div>

<h2 class="section-title abs consult-head"><span class="dash"></span>Consulting <b>Services</b></h2>
<div class="abs consult-copy">
  <p>Nemo enim ipsam voluptatem quia voluptas sit aspernatur aut odit aut fugit, sed quia consequuntur magni dolores eos qui ratione voluptatem sequi nesciunt. Neque porro quisquam est, qui dolorem ipsum quia dolor sit amet, consectetur, adipisci velit, sed quia non numquam eius modi tempora incidunt ut labore et dolore magnam aliquam quaerat voluptatem. Ut enim ad minima veniam, quis nostrum exercitationem ullam corporis suscipit laboriosam, nisi ut aliquid ex ea commodi consequatur.</p>
  <p style="margin-top:14px">Quis autem vel eum iure reprehenderit qui in ea voluptate velit esse quam nihil molestiae consequatur, vel illum qui dolorem eum fugiat quo voluptas nulla pariatur.</p>
</div>
<span class="btn-outline">Download the E-Book &#9656;</span>

<div class="abs diff-title">The Vorlant Difference</div>
<div class="accordion">
  <div class="acc-row">Information Protection<span class="sign">&minus;</span></div>
  <div class="acc-body">
    <div class="img" role="img" aria-label="Hand touching a cloud security icon on a digital screen"></div>
    <p>Nemo enim ipsam voluptatem quia voluptas sit aspernatur aut odit aut fugit, sed quia consequuntur magni dolores eos qui ratione voluptatem sequi nesciunt. Neque porro quisquam est, qui dolorem ipsum quia dolor sit amet, consectetur, adipisci velit, sed quia non.</p>
  </div>
  <div class="acc-row">Threat Protection<span class="sign">+</span></div>
  <div class="acc-row" style="border-bottom:0">Web and Cloud Protection<span class="sign">+</span></div>
</div>

<section class="team">
  <h2 class="section-title center abs" style="top:64px"><span class="dash"></span>Our Executive <b>Team</b><span class="dash"></span></h2>
</section>
<div class="member" style="left:163px">
  <div class="photo" role="img" aria-label="Photo of team member one"></div>
  <h4>Team Member 1</h4><div class="role">Expertise</div>
  <p>Sed ut perspiciatis unde omnis iste natus error sit voluptatem accusa ntium doloremque laudantium.</p>
  <div class="social"><i></i><i></i><i></i><i></i></div>
</div>
<div class="member" style="left:387px">
  <div class="photo" role="img" aria-label="Photo of team member two"></div>
  <h4>Team Member 2</h4><div class="role">Expertise</div>
  <p>Sed ut perspiciatis unde omnis iste natus error sit voluptatem accusa ntium doloremque laudantium.</p>
  <div class="social"><i></i><i></i><i></i><i></i></div>
</div>
<div class="member" style="left:611px">
  <div class="photo" role="img" aria-label="Photo of team member three"></div>
  <h4>Team Member 3</h4><div class="role">Expertise</div>
  <p>Sed ut perspiciatis unde omnis iste natus error sit voluptatem accusa ntium doloremque laudantium.</p>
  <div class="social"><i></i><i></i><i></i><i></i></div>
</div>
<div class="member" style="left:838px">
  <div class="photo" role="img" aria-label="Photo of team member four"></div>
  <h4>Team Member 4</h4><div class="role">Expertise</div>
  <p>Sed ut perspiciatis unde omnis iste natus error sit voluptatem accusa ntium doloremque laudantium.</p>
  <div class="social"><i></i><i></i><i></i><i></i></div>
</div>
<div class="v-dots"><i class="on"></i><i></i><i></i></div>

<h2 class="section-title center abs" style="top:2318px"><span class="dash"></span>Our <b>Blog</b><span class="dash"></span></h2>

<article class="post" style="left:163px">
  <div class="img" role="img" aria-label="City skyline at night with a life ring in the foreground"></div>
  <div class="date"><b>11</b><span>Dec, 2018</span></div>
  <div class="meta"><span>&#9679; By Admin</span><span>&#9632; Comments</span></div>
  <h4>Lorem ipsum dolor sit amet, consectetur adipiscing elit, sed do</h4>
  <p>Nemo enim ipsam voluptatem quia voluptas sit aspernatur aut odit aut fugit, sed quia consequuntur magni dolores eos qui ratione voluptatem sequi nesciunt.</p>
  <span class="more">Read More &#9656;</span>
</article>
<article class="post" style="left:461px">
  <div class="img" role="img" aria-label="City skyline at night with a life ring in the foreground"></div>
  <div class="date"><b>7</b><span>Dec, 2018</span></div>
  <div class="meta"><span>&#9679; By Admin</span><span>&#9632; Comments</span></div>
  <h4>Lorem ipsum dolor sit amet, consectetur adipiscing elit, sed do</h4>
  <p>Nemo enim ipsam voluptatem quia voluptas sit aspernatur aut odit aut fugit, sed quia consequuntur magni dolores eos qui ratione voluptatem sequi nesciunt.</p>
  <span class="more">Read More &#9656;</span>
</article>
<article class="post" style="left:761px">
  <div class="img" role="img" aria-label="City skyline at night with a life ring in the foreground"></div>
  <div class="date"><b>1</b><span>Dec, 2018</span></div>
  <div class="meta"><span>&#9679; By Admin</span><span>&#9632; Comments</span></div>
  <h4>Lorem ipsum dolor sit amet, consectetur adipiscing elit, sed do</h4>
  <p>Nemo enim ipsam voluptatem quia voluptas sit aspernatur aut odit aut fugit, sed quia consequuntur magni dolores eos qui ratione voluptatem sequi nesciunt.</p>
  <span class="more">Read More &#9656;</span>
</article>
<span class="btn-load">Load More Post</span>

<section class="contact">
  <div class="contact-panel"></div>
</section>
<div class="info-block" style="top:2968px">
  <div class="info-label">Locate Us</div>
  <p>Sed ut perspiciatis unde omnis iste natus<br>error sit voluptatem accusantium</p>
  <hr>
</div>
<div class="info-block" style="top:3057px">
  <div class="info-label">Contact Us</div>
  <p>+123 456 789<br>hello@talmerocharts.example</p>
  <hr>
</div>
<div class="info-block" style="top:3150px">
  <div class="info-label">Follow Us</div>
  <div class="follow"><i></i><i></i><i class="on"></i><i></i></div>
</div>

<h2 class="section-title abs touch-head"><span class="dash"></span>Get In <b>Touch</b></h2>
<p class="abs touch-copy">Please complete and submit this form and one of our representatives will reply promptly.</p>
<div class="field" style="left:687px;top:3063px;width:168px"><svg width="9" height="9" viewBox="0 0 9 9"><circle cx="4.5" cy="3" r="2.2" fill="#aaa"/><path d="M0.5 9a4 4 0 0 1 8 0z" fill="#aaa"/></svg>Your Name</div>
<div class="field" style="left:867px;top:3063px;width:170px"><svg width="10" height="8" viewBox="0 0 10 8"><rect x=".5" y=".5" width="9" height="7" fill="none" stroke="#aaa"/><path d="M.5.5 5 4.5 9.5.5" fill="none" stroke="#aaa"/></svg>Your Email</div>
<div class="field" style="left:687px;top:3110px;width:350px"><svg width="9" height="9" viewBox="0 0 9 9"><rect x=".5" y=".5" width="8" height="8" fill="none" stroke="#aaa"/></svg>Subject</div>
<div class="field" style="left:687px;top:3156px;width:350px;height:54px"><svg width="9" height="9" viewBox="0 0 9 9"><path d="M1 8 2 6 7 1l1 1-5 5z" fill="#aaa"/></svg>Message</div>
<span class="btn-submit">SUBMIT</span>

<footer class="site-footer"></footer>
<div class="footer-brand"><span class="brand-mark"></span><span class="brand-name">TALMERO CHARTS</span></div>
<div class="abs footer-about">
  <p>Lorem ipsum dolor sit amet, consectetur adipiscing elit, sed do eiusmod tempor incididunt ut labore et dolore magna aliqua. Ut enim ad minim veniam, quis nostrud exercitation ullamco laboris nisi ut aliquip ex ea commodo consequat. Duis aute irure dolor in reprehenderit</p>
  <p style="color:#fff;font-weight:700;margin-top:6px">Read More</p>
</div>
<div class="footer-col" style="left:461px">
  <h5>Quick Links</h5>
  <ul><li class="current">Home</li><li>About Us</li><li>Our Products</li><li>Consulting Services</li><li>Our Blog</li><li>Contact Us</li></ul>
</div>
<div class="footer-col" style="left:611px">
  <h5>Products &amp; Services</h5>
  <ul><li>Integrated Cyber Defense</li><li>Advanced Threat Protection</li><li>Information Protection</li><li>Endpoint Security</li><li>Email Security</li><li>Network Security</li><li>Cloud Security</li></ul>
</div>
<div class="footer-col subscribe" style="left:835px">
  <h5>Subscribe Us</h5>
  <p>Subscribe to our Newsletter to get latest news and updates about cyber security</p>
</div>
<div class="sub-input"><svg width="10" height="8" viewBox="0 0 10 8"><rect x=".5" y=".5" width="9" height="7" fill="none" stroke="#e2d6f0"/><path d="M.5.5 5 4.5 9.5.5" fill="none" stroke="#e2d6f0"/></svg>Your email Address</div>
<span class="btn-send">SEND</span>
<div class="footer-bar">&copy; 2018 Talmero Charts. All rights reserved.</div>

</body>
</html>
```